Need a book cover design for a Lumora Book on Herbal Remedies

I need a book cover for my new ebook, here are the details:
Title: Meadow Cures
Sub-Heading: Buried Ancient Garden Tonics
Reclaiming the Wisdom of Roots for Everyday Wellness and Strength
Author: Nora Belcourt

```html
<!DOCTYPE html>
<html lang="en">
<head>
<meta charset="utf-8">
<title>Meadow Cures — Nora Belcourt</title>
<link href="https://fonts.googleapis.com/css2?family=Andada+Pro:wght@700&family=Open+Sans:wght@300&display=swap" rel="stylesheet">
<style>
  :root {
    --cream: #ede4dc;
    --plum: #663352;
    --teal-deep: #0d6478;
    --teal-mid: #1f8a6c;
    --sage-text: #3b6b5e;
    --author-text: #f1e7e1;
  }
  html, body {
    margin: 0;
    padding: 0;
    overflow: hidden;
    background: var(--cream);
  }
  .cover {
    position: relative;
    width: 794px;
    height: 1200px;
    overflow: hidden;
    background: var(--cream);
  }
  .photo {
    position: absolute;
  }
  .photo--tea {
    left: 0; top: 0; width: 500px; height: 247px;
    background: linear-gradient(135deg, #e9e8e2 0%, #b9b08a 45%, #7d6a2e 70%, #c9c9c0 100%);
  }
  .photo--chives {
    left: 500px; top: 0; width: 294px; height: 295px;
    background: radial-gradient(circle at 55% 35%, #b77bc4 0%, #8ca74c 45%, #4f8a2f 100%);
  }
  .photo--lavender {
    left: 0; top: 764px; width: 229px; height: 320px;
    background: linear-gradient(180deg, #f4f2f2 0%, #e3c8d8 45%, #8b6cb8 85%, #6c4fa0 100%);
  }
  .photo--nettle {
    left: 229px; top: 838px; width: 565px; height: 246px;
    background: linear-gradient(160deg, #3f6b2c 0%, #4f8a35 35%, #c89d5e 65%, #4b3a2c 100%);
  }
  .title {
    position: absolute;
    left: 0; top: 340px; width: 794px;
    margin: 0;
    text-align: center;
    font-family: "Andada Pro", Georgia, serif;
    font-weight: 700;
    font-size: 134px;
    line-height: 148px;
    letter-spacing: 3px;
    text-transform: uppercase;
    background: radial-gradient(ellipse at 50% 50%, var(--teal-mid) 0%, #1c7f6a 45%, var(--teal-deep) 100%);
    -webkit-background-clip: text;
    background-clip: text;
    color: transparent;
  }
  .title-rule {
    position: absolute;
    left: 134px; top: 624px;
    width: 527px; height: 7px;
    background: var(--plum);
  }
  .subtitle {
    position: absolute;
    left: 0; top: 645px; width: 794px;
    margin: 0;
    text-align: center;
    font-family: "Open Sans", Arial, sans-serif;
    font-weight: 300;
    font-size: 24px;
    line-height: 36px;
    letter-spacing: 2px;
    color: var(--sage-text);
  }
  .author-band {
    position: absolute;
    left: 0; top: 1084px; width: 794px; height: 116px;
    background: var(--plum);
    display: flex;
    align-items: center;
    justify-content: center;
  }
  .author {
    margin: 0;
    font-family: "Open Sans", Arial, sans-serif;
    font-weight: 300;
    font-size: 54px;
    letter-spacing: 9px;
    text-transform: uppercase;
    color: var(--author-text);
  }
</style>
</head>
<body>
  <main class="cover">
    <div class="photo photo--tea" role="img" aria-label="Two glass cups of herbal tea with fresh mint and fennel leaves"></div>
    <div class="photo photo--chives" role="img" aria-label="Purple chive blossoms in a green meadow"></div>

    <h1 class="title">Meadow<br>Cures</h1>
    <div class="title-rule"></div>
    <p class="subtitle">Buried Ancient Garden Tonics<br>Reclaiming the Wisdom of Roots for<br>Everyday Wellness and Strength</p>

    <div class="photo photo--lavender" role="img" aria-label="Bottle of pink herbal oil with mortar and pestle and lavender sprigs"></div>
    <div class="photo photo--nettle" role="img" aria-label="Woven basket of nettle leaves and chamomile flowers beside a bottle of oil on a wooden table"></div>

    <footer class="author-band">
      <p class="author">Nora Belcourt</p>
    </footer>
  </main>
</body>
</html>
```